Business Cards for cafe providing speciality coffee and food

I need a business card design for my husband’s businesses. He has two cafes in Brisbane. The business name is Copperleaf Roasting House. They sell high end specialty coffee as well as breakfast and lunch. All the food is cooked fresh, in house and they have strict quality controls for their coffee. I would like the business card to feature the address for both cafes, my husband’s phone number and the business’s instagram. The address for the first is 61 Wexley Crescent, Pine Hollow and the second is 23 Dorrit Avenue, Sallowmere. The Instagram handle is @copperleafroastinghouse and phone number is 0491326085. We already have a business logo that is attached.

Target Market(s)

All ages, higher disposable income and more likely to eat out regularly

Industry/Entity Type

Hospitality

Contact Information for Business Card

Must be suitable for both customers and suppliers

Font styles to use
Sans Serif

Colors

Designer to choose colors to be used in the design.

Requirements
Must have
• Owner’s name: Griff Tallant
• Addresses of both cafes: 61 Wexley Crescent, Pine Hollow and 23 Dorrit Avenue, Sallowmere
• Instagram handle: @copperleafroastinghouse
• Contact number: 0491326085
Nice to have
• Business logo

```html
<!DOCTYPE html>
<html lang="en">
<head>
<meta charset="utf-8">
<title>Copperleaf Roasting House – Business Card</title>
<link rel="stylesheet" href="https://fonts.googleapis.com/css2?family=Lato:wght@400;700&family=Roboto:wght@700&display=swap">
<style>
  :root {
    --page-bg: #e6e4e2;
    --card-white: #ffffff;
    --card-mist: #f0efee;
    --ink: #0a0a0a;
    --on-ink: #ffffff;
    --on-ink-soft: #d9d9d9;
  }
  * { margin: 0; padding: 0; box-sizing: border-box; }
  html, body {
    width: 1200px;
    height: 900px;
    overflow: hidden;
    background: var(--page-bg);
  }
  .card {
    position: absolute;
    left: 180px;
    top: 190px;
    width: 840px;
    height: 519px;
    overflow: hidden;
    background: linear-gradient(180deg, var(--card-white) 0%, var(--card-mist) 60%);
    box-shadow: 0 6px 24px rgba(0,0,0,0.12);
    font-family: "Lato", sans-serif;
  }
  .card-band {
    position: absolute;
    inset: 0;
  }
  .brand {
    position: absolute;
    left: 0;
    right: 0;
    top: 128px;
    display: flex;
    align-items: center;
    justify-content: center;
    gap: 14px;
  }
  .brand-dot {
    width: 22px;
    height: 22px;
    border-radius: 50%;
    background: var(--ink);
  }
  .brand-name {
    font-family: "Lato", sans-serif;
    font-weight: 700;
    font-size: 30px;
    letter-spacing: 2px;
    text-transform: uppercase;
    color: var(--ink);
  }
  .owner {
    position: absolute;
    right: 450px;
    top: 370px;
    text-align: right;
  }
  .owner-name {
    font-family: "Roboto", sans-serif;
    font-weight: 700;
    font-size: 31px;
    color: var(--on-ink);
    text-transform: uppercase;
    white-space: nowrap;
  }
  .address {
    position: absolute;
    top: 450px;
    font-size: 22px;
    color: var(--on-ink-soft);
    white-space: nowrap;
  }
  .address--first { right: 450px; text-align: right; }
  .address--second { left: 477px; }
  .divider {
    position: absolute;
    left: 420px;
    top: 370px;
    width: 2px;
    height: 110px;
    background: var(--on-ink);
  }
  .contact-list {
    position: absolute;
    left: 442px;
    top: 372px;
    list-style: none;
  }
  .contact-item {
    display: flex;
    align-items: center;
    gap: 8px;
    height: 30px;
    font-size: 22px;
    color: var(--on-ink-soft);
    white-space: nowrap;
  }
  .contact-icon {
    width: 26px;
    height: 26px;
    flex: none;
  }
</style>
</head>
<body>
  <main class="card">
    <svg class="card-band" width="840" height="519" viewBox="0 0 840 519" aria-hidden="true">
      <path d="M0 292 H335 C365 292 370 322 420 322 C470 322 475 292 505 292 H840"
            fill="none" stroke="var(--ink)" stroke-width="4"/>
      <path d="M0 300 H330 C362 300 366 330 420 330 C474 330 478 300 510 300 H840 V519 H0 Z"
            fill="var(--ink)"/>
    </svg>

    <div class="brand">
      <span class="brand-dot"></span>
      <span class="brand-name">Copperleaf Roasting House</span>
    </div>

    <div class="owner">
      <p class="owner-name">Griff Tallant</p>
    </div>
    <p class="address address--first">61 Wexley Crescent, Pine Hollow</p>

    <div class="divider"></div>

    <ul class="contact-list">
      <li class="contact-item">
        <svg class="contact-icon" viewBox="0 0 26 26" aria-hidden="true">
          <circle cx="13" cy="13" r="12" fill="var(--on-ink)"/>
          <path d="M6.5 10.5 C6.5 8 19.5 8 19.5 10.5 L18.5 12 L16 11 L16 9.8 C14 9.2 12 9.2 10 9.8 L10 11 L7.5 12 Z
                   M9 13 H17 L18.5 18.5 H7.5 Z" fill="var(--ink)"/>
          <circle cx="13" cy="15.5" r="1.6" fill="var(--on-ink)"/>
        </svg>
        <span>0491326085</span>
      </li>
      <li class="contact-item">
        <svg class="contact-icon" viewBox="0 0 26 26" aria-hidden="true">
          <circle cx="13" cy="13" r="12" fill="var(--on-ink)"/>
        </svg>
        <span>@copperleafroastinghouse</span>
      </li>
    </ul>
    <p class="address address--second">23 Dorrit Avenue, Sallowmere</p>
  </main>
</body>
</html>
```